Hotel Business Card Project

Amber Crest Hotel will be a premium boutique hotel in Dhaka, Bangladesh. The hotel will offer the finest amenities and facilities available on the market, and the cost per room investment will far exceed other 5-star hotels currently in the market.

As a result, we wanted the business card to reflect that premium/luxurious/upscale feel, and also be elegant and hospitable at the same time.

The name 'Amber Crest' is derived from the fact that Bangladesh has 6 distinct seasons (you can get more information online if required, or contact me about it). The leaves in the logo has the tree because trees give people shade, protection and safety (just like our hotel would try to give).

Target Market(s)

Business professionals, guests

Industry/Entity Type

Investment

Requirements
Must have
• Elegant, Classy and very attractive business card.

Must be editable to enter specific Names, Positions, Phone numbers and email later on.
Nice to have
• The address would be: House 47, Road 23, Lakeview 5, Dhaka 1208, Bangladesh

Slogan- Luxury Redefined

```html
<!DOCTYPE html>
<html lang="en">
<head>
<meta charset="utf-8">
<title>Amber Crest Hotel – Business Cards</title>
<link href="https://fonts.googleapis.com/css2?family=Marcellus&family=Arimo:wght@400;700&display=swap" rel="stylesheet">
<style>
  :root {
    --page: #e4e4e4;
    --paper: #ffffff;
    --bark: #3b2416;
    --lime: #c8da2b;
    --stone: #6d6e70;
    --amber: #d98c4a;
    --card-w: 494px;
    --card-h: 282px;
  }
  * { box-sizing: border-box; margin: 0; padding: 0; }
  html, body {
    width: 1200px; height: 756px; overflow: hidden;
    background: var(--page);
  }
  .sheet { position: relative; width: 1200px; height: 756px; }
  .card {
    position: absolute;
    width: var(--card-w); height: var(--card-h);
    overflow: hidden;
  }
  .card--contact { left: 73px; top: 72px; background: var(--paper); }
  .card--white   { left: 633px; top: 72px; background: var(--paper); }
  .card--lime    { left: 73px; top: 401px; background: var(--lime); }
  .card--bark    { left: 633px; top: 401px; background: var(--bark); }

  .swoosh { position: absolute; inset: 0; width: 100%; height: 100%; }

  .brand {
    position: absolute;
    display: flex; flex-direction: column; align-items: center;
    font-family: "Marcellus", serif;
    white-space: nowrap;
  }
  .brand__dot { border-radius: 50%; }
  .brand__name { letter-spacing: 0.5px; }

  .card--contact .brand { left: 10px; width: 230px; top: 70px; }
  .card--contact .brand__dot { width: 78px; height: 78px; background: var(--amber); margin-bottom: 24px; }
  .card--contact .brand__name { font-size: 22px; color: var(--stone); }

  .card--white .brand,
  .card--lime .brand,
  .card--bark .brand { left: 0; right: 0; top: 46px; }
  .card--white .brand__dot,
  .card--lime .brand__dot,
  .card--bark .brand__dot { width: 120px; height: 120px; margin-bottom: 30px; }
  .card--white .brand__dot { background: var(--amber); }
  .card--lime .brand__dot { background: var(--bark); }
  .card--bark .brand__dot { background: var(--paper); }
  .card--white .brand__name,
  .card--lime .brand__name,
  .card--bark .brand__name { font-size: 38px; }
  .card--white .brand__name { color: var(--stone); }
  .card--lime .brand__name { color: var(--bark); }
  .card--bark .brand__name { color: var(--paper); }

  .contact {
    position: absolute; right: 23px; top: 58px;
    text-align: right;
    font-family: "Arimo", sans-serif;
    color: var(--paper);
  }
  .contact__name { font-weight: 700; font-size: 17px; color: var(--lime); line-height: 1.1; }
  .contact__title { font-size: 13px; letter-spacing: 1px; line-height: 1.2; }
  .contact__lines { list-style: none; margin-top: 24px; font-size: 12.5px; }
  .contact__lines li { display: flex; justify-content: flex-end; align-items: center; gap: 4px; line-height: 21px; }
  .contact__lines svg { width: 10px; height: 10px; fill: none; stroke: var(--paper); stroke-width: 1.4; }
  .contact__address { margin-top: 14px; font-size: 12.5px; line-height: 17px; font-style: normal; }
</style>
</head>
<body>
<main class="sheet">

  <section class="card card--contact">
    <svg class="swoosh" viewBox="0 0 494 282" preserveAspectRatio="none" aria-hidden="true">
      <path d="M300 0 C332 118 272 230 156 282 L494 282 L494 0 Z" fill="var(--lime)"/>
      <path d="M311 0 C342 118 286 232 178 282 L494 282 L494 0 Z" fill="var(--paper)"/>
      <path d="M316 0 C346 118 292 232 186 282 L494 282 L494 0 Z" fill="var(--bark)"/>
    </svg>
    <div class="brand">
      <span class="brand__dot"></span>
      <span class="brand__name">Amber Crest Hotel</span>
    </div>
    <div class="contact">
      <p class="contact__name">Your Name</p>
      <p class="contact__title">Title</p>
      <ul class="contact__lines">
        <li><svg viewBox="0 0 10 10"><path d="M2 1 L4 1 L4.5 3 L3.3 4 Q4.3 6 6 6.7 L7 5.5 L9 6 L9 8 Q5 9.5 1 3 Z"/></svg>123-456-7890</li>
        <li><svg viewBox="0 0 10 10"><rect x="1" y="2" width="8" height="6"/><path d="M1 2 L5 5.5 L9 2"/></svg>info@ambercrest.com</li>
        <li><svg viewBox="0 0 10 10"><circle cx="5" cy="5" r="4"/><path d="M1 5 H9 M5 1 Q2.5 5 5 9 M5 1 Q7.5 5 5 9"/></svg>www.ambercrest.com</li>
      </ul>
      <address class="contact__address">House 47, Road 23<br>Lakeview 5, Dhaka 1208<br>Bangladesh</address>
    </div>
  </section>

  <section class="card card--white">
    <div class="brand"><span class="brand__dot"></span><span class="brand__name">Amber Crest Hotel</span></div>
  </section>

  <section class="card card--lime">
    <div class="brand"><span class="brand__dot"></span><span class="brand__name">Amber Crest Hotel</span></div>
  </section>

  <section class="card card--bark">
    <div class="brand"><span class="brand__dot"></span><span class="brand__name">Amber Crest Hotel</span></div>
  </section>

</main>
</body>
</html>
```